K.T.L Electrical Services Pty Ltd

Electrical contracting business. I have a base for the design which i like. The contact number needs to be changed to 0491736250 and the O made more solid and level with the rest of the letters. If you have any other ideas of what would make it better I'm happy to see them.

The back side to be written as dot points with the following:
- Residential & Commercial
- Maintenance
- PV & Battery servicing
- EV Chargers

```html
<!DOCTYPE html>
<html lang="en">
<head>
<meta charset="utf-8">
<title>K.T.L Electrical Services – Business Cards</title>
<link rel="stylesheet" href="https://fonts.googleapis.com/css2?family=Montserrat:wght@500;600;700&display=swap">
<style>
  :root {
    --bg: #1c1c1e;
    --card-dark: #2a2a2c;
    --card-dark-2: #353537;
    --card-light: #ffffff;
    --brand-blue: #3f9fdc;
    --brand-yellow: #f5c400;
    --text-light: #ffffff;
    --text-grey: #555a60;
    --text-dark: #2b2b2d;
  }
  * { box-sizing: border-box; margin: 0; padding: 0; }
  html, body { width: 1200px; height: 886px; overflow: hidden; }
  body {
    background: var(--bg);
    font-family: "Montserrat", Arial, sans-serif;
    position: relative;
  }
  .card {
    position: absolute;
    left: 250px;
    width: 700px;
    height: 400px;
    border-radius: 28px;
    overflow: hidden;
    box-shadow: 0 14px 30px rgba(0,0,0,.45);
  }
  /* ---------- back ---------- */
  .card--back { top: 30px; background: var(--card-dark); }
  .back-pattern {
    position: absolute; inset: 0;
    background: radial-gradient(ellipse at 70% 20%, #4a4a4d 0%, var(--card-dark-2) 40%, var(--card-dark) 80%);
  }
  .back-content {
    position: absolute; inset: 0;
    display: flex; flex-direction: column; align-items: center; justify-content: center;
    gap: 26px;
  }
  .brand { display: flex; align-items: center; gap: 14px; }
  .brand-dot {
    width: 62px; height: 62px; border-radius: 50%;
    background: var(--brand-blue);
    flex: none;
  }
  .brand-name {
    color: var(--brand-blue); font-weight: 700; line-height: 1;
    display: flex; flex-direction: column;
  }
  .brand-name .brand-main { font-size: 74px; letter-spacing: 2px; }
  .brand-name .brand-sub { font-size: 20px; letter-spacing: 1.5px; margin-top: 4px; }
  .service-list {
    list-style: none;
    display: grid; grid-template-columns: auto auto; column-gap: 40px; row-gap: 10px;
    color: var(--text-light); font-size: 21px; font-weight: 500;
  }
  .service-list li::before {
    content: ""; display: inline-block; width: 9px; height: 9px; border-radius: 50%;
    background: var(--brand-yellow); margin-right: 10px; vertical-align: middle;
  }
  /* ---------- front ---------- */
  .card--front { top: 456px; background: var(--card-light); }
  .plug-art { position: absolute; inset: 0; }
  .front-content { position: absolute; left: 44px; top: 40px; width: 400px; }
  .brand--front .brand-dot { width: 56px; height: 56px; }
  .brand--front .brand-main { font-size: 64px; }
  .brand--front .brand-sub { font-size: 18px; }
  .person { margin-top: 30px; }
  .person-name { color: var(--brand-blue); font-weight: 700; font-size: 24px; letter-spacing: 1px; text-transform: uppercase; }
  .person-role { color: var(--text-grey); font-size: 17px; font-weight: 500; margin-top: 2px; }
  .address { margin-top: 18px; color: var(--text-grey); font-size: 17px; line-height: 1.35; }
  .contacts { list-style: none; margin-top: 18px; color: var(--text-dark); font-size: 17px; }
  .contacts li { display: flex; align-items: center; gap: 10px; margin-bottom: 6px; }
  .contacts svg { width: 18px; height: 18px; flex: none; }
</style>
</head>
<body>

<section class="card card--back" aria-label="Card back">
  <div class="back-pattern" role="img" aria-label="Repeating embossed pattern of circled plug motifs on dark card"></div>
  <div class="back-content">
    <div class="brand brand--back">
      <span class="brand-dot"></span>
      <span class="brand-name"><span class="brand-main">K.T.L</span><span class="brand-sub">ELECTRICAL SERVICES</span></span>
    </div>
    <ul class="service-list">
      <li>Residential &amp; Commercial</li>
      <li>Maintenance</li>
      <li>PV &amp; Battery servicing</li>
      <li>EV Chargers</li>
    </ul>
  </div>
</section>

<section class="card card--front" aria-label="Card front">
  <svg class="plug-art" viewBox="0 0 700 400" preserveAspectRatio="none">
    <path d="M400 0 H700 V400 H540 C500 300 470 210 430 140 C410 100 395 50 400 0 Z"
          fill="#2a2a2c" role="img" aria-label="Large blue outlined electric plug illustration with yellow lightning bolt on dark panel"/>
  </svg>
  <div class="front-content">
    <div class="brand brand--front">
      <span class="brand-dot"></span>
      <span class="brand-name"><span class="brand-main">K.T.L</span><span class="brand-sub">ELECTRICAL SERVICES</span></span>
    </div>
    <div class="person">
      <p class="person-name">Daniel Harper</p>
      <p class="person-role">Manager</p>
    </div>
    <p class="address">Your Address, City<br>State, Zip 0000</p>
    <ul class="contacts">
      <li>
        <svg viewBox="0 0 24 24"><path fill="#3f9fdc" d="M6.6 10.8a15 15 0 0 0 6.6 6.6l2.2-2.2a1 1 0 0 1 1-.25 11.4 11.4 0 0 0 3.6.57 1 1 0 0 1 1 1V20a1 1 0 0 1-1 1A17 17 0 0 1 3 4a1 1 0 0 1 1-1h3.5a1 1 0 0 1 1 1c0 1.25.2 2.45.57 3.57a1 1 0 0 1-.25 1z"/></svg>
        0491736250
      </li>
      <li>
        <svg viewBox="0 0 24 24"><rect x="2" y="5" width="20" height="14" rx="2" fill="#3f9fdc"/><path d="M3 6l9 7 9-7" fill="none" stroke="#fff" stroke-width="1.8"/></svg>
        youremail@example.com
      </li>
      <li>
        <svg viewBox="0 0 24 24"><circle cx="12" cy="12" r="10" fill="#3f9fdc"/><path d="M2 12h20M12 2c3 3 3 17 0 20M12 2c-3 3-3 17 0 20" fill="none" stroke="#fff" stroke-width="1.4"/></svg>
        www.example.com
      </li>
    </ul>
  </div>
</section>

</body>
</html>
```